Web Design Project- eLearning Company

Hello Designers,
We just successfully used pixel-forge to design the logo of our new company, and would like to now accept submissions for design of our website. We have seen several creative designs out there in pixelforge, and hope to use your skills to develop a highly professional site that sets us apart and quickly conveys our offering to the viewer.
About the Company: Vendaroo is a new eLearning company, based in India. We plan to develop and offer complete eLearning solutions to companies in India. Please note that we are not targeting consumers or students. Our website will be viewed by middle management/senior management executives of large companies and needs to have a look-n-feel that establishes ourselves as a leader in this space.
What do we offer? We aim to offer a complete eLearning solution that will enable our customer to roll-out and execute an eLearning program for its employees, field sales teams, business ecosystem (resellers/distributors), brand franchisees or dealers.
Components of our offering: In order to be a one-stop shop for our customer, we offer all the components required for them to successfully roll out a Learning program. The homepage *needs to showcase * this.
This includes -
(1) the technology platform (LMS or Learning Management System) which hosts the content and provides administrative features and maintains database of learning records, scores etc.. See quendrix.example for a view on how these work.
(2) the actual learning content that we will develop for them. We will build a library of generic content, but initially the emphasis should be on custom content development. This includes interactive course material and assessments. See morvela.example or tessubrook.example for this.
(3) administrative services to help customers plan, execute and collect data. We will offer helpdesk services to learners and training administrators so that client does not waste time and efforts in driving this initiative- We will manage it for them. The following link shows another company's similar service offering:
http://www.brightholm.example/services/Learning-Services/Learning-Operations/Learning-Support-Services
The Job:
We need a home page, as well as the following pages to be designed:
1. HomePage
2. About Us
3. Products and Services
4. News & Blog
5. Contact us
Design guidelines:
-Colors:I have uploaded our corporate logo. Either the logo colors can be used, or the color theme needs to be in harmony with the logo colors. I would like to see different styles before we can begin to narrow down on a particular style. Having a slider at the top with 3-4 slides would be worth checking out.
Content:
-Home Page: Slider, a client testimonial box, a graphic that showcases our 3-pillar offering (Platform+ content + administrative services) and a box showcasing the latest news release. Designers are welcome to stray from this and present alternate designs. In fact, we encourage you to be creative.
- Other pages- Similar to any standard corporate site.
- All Pages have to be SEO friendly.
CMS- Drupal/Joomla
Updates
websites that are worth looking into to get a feel of the breadth of our offering, and the look we aim for:
glimmerpath.example
brightholm.example
Hello Designers,
We would love to receive more designs from all of you. So far, none of the designs have hit the right buttons, the contest is therefore wide open and completely up for grabs !
As an update, we have now committed on the project funds, as we are confident that by the end of the content we will have a design that we can take to production.
Do feel free to shoot me any questions, concerns or suggestions that you may have. We will respond to all queries.
Cheers and Happy Designing !
Hello Designers,
The original content closing date is tomorrow (Saturday). If there are designers that are working on designs and need more time, then please let me know so that I can extend the deadline.
I encourage you to actively participate, the contest is still open.
Thanks.
I have added another image file that has our company logo done in a stylized fashion. You were welcome to use this as well.

```html
<!DOCTYPE html>
<html lang="en">
<head>
<meta charset="utf-8">
<title>Vendaroo – Products &amp; Services</title>
<link href="https://fonts.googleapis.com/css2?family=Open+Sans:wght@300;400;500;600;700&display=swap" rel="stylesheet">
<style>
:root{
  --green:#7ab51d;
  --green-dark:#5f9412;
  --nav:#3f4448;
  --ink:#222;
  --muted:#777;
  --soft:#f1f1f1;
  --line:#dcdcdc;
  --footer:#3d4246;
}
*{box-sizing:border-box;margin:0;padding:0}
html,body{width:727px;height:1200px;overflow:hidden}
body{position:relative;background:#fff;font-family:"Open Sans",Arial,sans-serif;color:var(--ink)}
.abs{position:absolute}
.top-rule{left:0;top:0;width:727px;height:3px;background:var(--green)}
.signup{left:561px;top:3px;width:93px;height:19px;background:var(--green);color:#fff;font-size:7.5px;font-weight:700;text-align:center;line-height:19px;border-radius:0 0 2px 2px}
.brand{left:72px;top:30px;display:flex;align-items:center;gap:7px}
.brand-mark{width:26px;height:26px;background:var(--green);border-radius:4px}
.brand-name{font-size:23px;font-weight:700;color:#4a4f53;letter-spacing:-.5px;line-height:1}
.search{left:507px;top:46px;width:147px;height:18px;border:1px solid #ccc;border-radius:2px;background:#f7f7f7;font-size:6.5px;color:#aaa;padding:5px 7px}
.search svg{position:absolute;right:5px;top:4px}
.nav{left:0;top:89px;width:727px;height:35px;background:var(--nav)}
.nav a{position:absolute;top:12px;font-size:8.5px;color:#fff;text-decoration:none}
.nav a.active{top:9px;height:16px;line-height:16px;padding:0 7px;background:var(--green);border-radius:2px;font-weight:600}
.social{display:flex;gap:7px}
.social span{width:16px;height:16px;background:#8a9094;border-radius:3px;display:block}
.nav .social{position:absolute;left:587px;top:10px}
.hero{left:0;top:124px;width:727px;height:154px;background:var(--soft)}
.hero h1{left:72px;top:38px;font-size:22px;font-weight:300;color:#222}
.hero h1 b{font-weight:400;color:var(--green)}
.hero p{left:72px;top:70px;width:250px;font-size:8.6px;line-height:11px;color:#777}
.devices{left:340px;top:146px;width:314px;height:138px;background:linear-gradient(135deg,#d9d9d9,#9aa 55%,#3a3d40);border-radius:4px}
.intro{left:73px;top:300px;width:585px;font-size:10.6px;line-height:17px;color:#222}
.divider{left:80px;width:572px;height:10px;background:radial-gradient(ellipse at 50% 0,rgba(0,0,0,.06),rgba(0,0,0,0) 70%)}
.disc{left:101px;width:158px;height:158px;border-radius:50%;border:1px solid #e3e3e3;box-shadow:0 0 4px rgba(0,0,0,.06)}
.svc h2{position:absolute;left:314px;font-size:20.5px;font-weight:500;color:#111;white-space:nowrap}
.svc p{position:absolute;left:314px;width:320px;font-size:10.8px;line-height:15.5px;color:#888;font-weight:400}
.btn{position:absolute;left:315px;width:86px;height:22px;background:linear-gradient(#a5d16b,#7fb53a);border:1px solid #6c9c2d;border-radius:2px;color:#2f4a0d;font-size:8.5px;font-weight:600;text-align:center;line-height:20px}
.footer{left:0;top:969px;width:727px;height:199px;background:var(--soft)}
.footer h3{position:absolute;top:18px;font-size:12.5px;font-weight:400;color:#222}
.news-title{left:73px;top:48px;font-size:9.5px;font-weight:600;color:#333}
.news-date{left:73px;top:66px;font-size:7px;color:#888}
.news-body{left:73px;top:82px;width:170px;font-size:6.8px;line-height:14px;color:#444}
.news-link{left:73px;top:163px;font-size:7px;color:#888}
.dots{left:437px;top:37px;display:flex;gap:3px}
.dots i{width:3px;height:3px;border-radius:50%;background:#ccc;display:block}
.dots i:last-child{background:#888}
.quote{left:252px;top:48px;width:202px;height:106px;background:#fff;border:1px solid #ddd;padding:20px 20px;font-size:6.7px;line-height:14px;color:#444}
.quote .mark{position:absolute;right:12px;bottom:6px;font-size:16px;font-weight:700;color:#444}
.cite{left:360px;top:164px;font-size:6.8px;color:#333;font-weight:600}
.cite em{font-style:normal;color:#e8511d}
.nl-text{left:491px;top:41px;width:160px;font-size:7.5px;line-height:11px;color:#222}
.nl-input{left:490px;top:69px;width:162px;height:24px;background:#fff;border:1px solid #ddd;border-radius:2px}
.nl-submit{left:598px;top:101px;width:54px;height:16px;background:linear-gradient(#a5d16b,#7fb53a);border:1px solid #6c9c2d;border-radius:2px;font-size:7px;color:#2f4a0d;text-align:center;line-height:14px}
.nl-rule{left:493px;top:126px;width:159px;height:1px;background:#ccc}
.stay{left:494px;top:133px;font-size:12.5px;color:#222}
.footer .social{position:absolute;left:497px;top:159px}
.bottom{left:0;top:1168px;width:727px;height:32px;background:var(--footer);color:#fff;font-size:7px}
.bottom nav{position:absolute;left:81px;top:11px;display:flex;gap:8px}
.bottom nav span.sep{color:#aaa}
.bottom .copy{position:absolute;left:497px;top:12px}
</style>
</head>
<body>
<div class="abs top-rule"></div>
<div class="abs signup">SIGN UP NOW!</div>

<header>
  <div class="abs brand"><span class="brand-mark"></span><span class="brand-name">Vendaroo</span></div>
  <div class="abs search">search
    <svg width="10" height="10" viewBox="0 0 10 10"><circle cx="4" cy="4" r="3" fill="none" stroke="#111" stroke-width="1.4"/><line x1="6.2" y1="6.2" x2="9" y2="9" stroke="#111" stroke-width="1.6"/></svg>
  </div>
</header>

<nav class="abs nav">
  <a style="left:73px">Home</a>
  <a style="left:119px">About Us</a>
  <a class="active" style="left:170px">Products</a>
  <a style="left:236px">News &amp; Blog</a>
  <a style="left:309px">Careers</a>
  <a style="left:354px">Contact Us</a>
  <div class="social"><span aria-label="Social link"></span><span aria-label="Social link"></span><span aria-label="Social link"></span></div>
</nav>

<section class="abs hero">
  <h1 class="abs">Our <b>Products &amp; Services</b></h1>
  <p class="abs">Utilizing the latest technologies, our solutions are designed to cater to diverse learning needs and devices. So whatever your learning need be, we have the right solution.</p>
</section>
<div class="abs devices" role="img" aria-label="Vendaroo platform shown on browser, desktop monitor and two phones"></div>

<p class="abs intro">We provide a wide range of award–winning learning solutions that can help you achieve business goals through enhanced performance. In this quest to improve performance in organizations through learning, we have earned the confidence of our clients and have won several awards and other recognitions too – a true testimony to our success.</p>

<div class="abs divider" style="top:372px"></div>
<div class="abs disc" style="top:390px;background:radial-gradient(circle,#6d8fb0 0,#b9c7d4 45%,#fff 70%)" role="img" aria-label="Software box with disc"></div>
<section class="svc">
  <h2 style="top:408px">Technology Platform</h2>
  <p style="top:446px">A winner of over 10 awards and recognition, NimbusLMS will not just amaze you with its stunning GUI, but its 160+ features will make your learning management easy and effective.</p>
  <div class="btn" style="top:509px">LEARN MORE</div>
</section>

<div class="abs divider" style="top:566px"></div>
<div class="abs disc" style="top:586px;background:radial-gradient(circle at 50% 45%,#6b5a6e 0,#b7a9b5 40%,#f4f2f3 72%)" role="img" aria-label="Woman working on a laptop"></div>
<section class="svc">
  <h2 style="top:601px">Content Development Services</h2>
  <p style="top:639px">A winner of over 10 awards and recognition, NimbusLMS will not just amaze you with its stunning GUI, but its 160+ features will make your learning management easy and effective.</p>
  <div class="btn" style="top:702px">LEARN MORE</div>
</section>

<div class="abs divider" style="top:764px"></div>
<div class="abs disc" style="top:782px;background:radial-gradient(circle at 50% 40%,#7a5a48 0,#c9b8ae 40%,#e9eef4 72%)" role="img" aria-label="Support agent wearing a headset"></div>
<section class="svc">
  <h2 style="top:799px">Administrative BPO services</h2>
  <p style="top:837px">A winner of over 10 awards and recognition, NimbusLMS will not just amaze you with its stunning GUI, but its 160+ features will make your learning management easy and effective.</p>
  <div class="btn" style="top:900px">LEARN MORE</div>
</section>

<footer class="abs footer">
  <h3 style="left:73px">Latest News</h3>
  <div class="abs news-title">Lorem ipsum dolor sit amet</div>
  <div class="abs news-date">14<sup style="font-size:5px">th</sup> November</div>
  <p class="abs news-body">Nam libero tempore, cum soluta nobis est eligendi optio cumque nihil impedit quo lorem ipsum dolor sit minus id quod maxime placeat facere possimus, omnis voluptas assumenda est, omnis dolor repellendus...</p>
  <div class="abs news-link">FULL ARTICLE &nbsp;›</div>

  <h3 style="left:254px">Testimonials</h3>
  <div class="abs dots"><i></i><i></i><i></i></div>
  <blockquote class="abs quote">At vero eos et accusamus et lucero iusto odio dignissimos ducimus qui blanditiis praesentium voluptatum deleniti atque corrupti quos dolores et quas molestias excepturi sint occaecati cupiditate non provident.<span class="mark">”</span></blockquote>
  <div class="abs cite">John Doe, <em>xyz etc.</em>, cat lover</div>

  <h3 style="left:491px">Signup for our newsletter</h3>
  <p class="abs nl-text">Enter your email address below to subscribe for our newsletter</p>
  <div class="abs nl-input"></div>
  <div class="abs nl-submit">submit</div>
  <div class="abs nl-rule"></div>
  <div class="abs stay">Stay Connected</div>
  <div class="social"><span aria-label="Social link"></span><span aria-label="Social link"></span><span aria-label="Social link"></span></div>
</footer>

<div class="abs bottom">
  <nav><span>Home</span><span class="sep">|</span><span>About Us</span><span class="sep">|</span><span>Products</span><span class="sep">|</span><span>News &amp; Blog</span><span class="sep">|</span><span>Contact Us</span></nav>
  <div class="copy">Copyright©2013 Vendaroo. All Rights Reserved</div>
</div>
</body>
</html>
```